BLUE FORGE (Business Card for Training Company)

Blue Forge is a training and consultancy company with a focus on executive protection and medical. I would like the card to be nice and sharp, not overdone and in black and red. I would also like it to highlight that it is "A Tavmont Company"

I would like it to be simple and highlight a few things.

1. Name
2. Title
3. Phone Number
4. Email

I would also like www.tavmontgroup.example/blue-forge to be on the card somewhere.

Target Market(s)

Security Companies

Industry/Entity Type

Security

Contact Information for Business Card

Blue Forge is a training and consultancy company with a focus on executive protection and medical. I would like the card to be nice and sharp, not overdone and in black and red. I would also like it to highlight that it is "A Tavmont Company" I would like it to be simple and highlight a few things. 1. Name 2. Title 3. Phone Number 4. Email I would also like www.tavmontgroup.example/blue-forge to be on the card somewhere.

Requirements
Must have
• A Tavmont Company listed on the card and the website
Nice to have
• Highlight Medical Training, Consultancy & Executive Protection Courses

```html
<!DOCTYPE html>
<html lang="en">
<head>
<meta charset="utf-8">
<title>Blue Forge – Business Card</title>
<link href="https://fonts.googleapis.com/css2?family=Audiowide&family=Roboto:wght@400&display=swap" rel="stylesheet">
<style>
  :root {
    --backdrop: #2a2a2a;
    --card: #171717;
    --card-deep: #050505;
    --red: #a01c21;
    --white: #f1f1f1;
    --embossed: #3a3a3a;
    --display: "Audiowide", sans-serif;
    --body: "Roboto", sans-serif;
  }
  * { box-sizing: border-box; margin: 0; padding: 0; }
  html, body { width: 1200px; height: 1138px; overflow: hidden; background: var(--backdrop); }
  .card {
    position: absolute;
    left: 275px;
    width: 620px;
    height: 375px;
    border-radius: 16px;
    overflow: hidden;
  }
  .card-front {
    top: 186px;
    background: linear-gradient(180deg, #1c1c1c 0%, #0d0d0d 55%, var(--card-deep) 100%);
  }
  .card-back { top: 608px; background: var(--card); }

  .front-mark {
    position: absolute;
    left: 0; right: 0; top: 108px;
    text-align: center;
    font-family: var(--display);
    font-size: 64px;
    line-height: 66px;
    color: var(--embossed);
    letter-spacing: 2px;
  }
  .front-url {
    position: absolute;
    left: 0; right: 0; top: 334px;
    display: flex; justify-content: center; align-items: center; gap: 14px;
    font-family: var(--body);
    font-size: 16px;
    color: var(--white);
  }
  .front-url svg { display: block; }

  .accent-dot {
    position: absolute;
    left: -24px; top: 44px;
    width: 38px; height: 76px;
    border-radius: 0 38px 38px 0;
    background: var(--red);
  }
  .holder-name {
    position: absolute;
    left: 29px; top: 57px;
    font-family: var(--display);
    font-size: 22px;
    color: var(--red);
  }
  .holder-title {
    position: absolute;
    left: 29px; top: 83px;
    font-family: var(--body);
    font-size: 16px;
    color: var(--white);
  }
  .back-mark {
    position: absolute;
    right: 34px; top: 50px;
    text-align: right;
    font-family: var(--display);
    font-size: 50px;
    line-height: 52px;
    color: var(--white);
  }
  .contact-list {
    position: absolute;
    left: 30px; top: 266px;
    list-style: none;
    font-family: var(--body);
    font-size: 16px;
    color: var(--white);
  }
  .contact-list li { display: flex; align-items: center; height: 23px; }
  .contact-list svg { width: 14px; height: 14px; margin-right: 16px; fill: var(--red); }
  .parent-company {
    position: absolute;
    right: 34px; top: 290px;
    text-align: right;
    font-family: var(--display);
    font-size: 18px;
    line-height: 22px;
    color: var(--white);
  }
</style>
</head>
<body>
  <section class="card card-front">
    <div class="front-mark">BLUE<br>FORGE</div>
    <div class="front-url">
      <svg width="48" height="8" viewBox="0 0 48 8"><line x1="6" y1="4" x2="48" y2="4" stroke="#f1f1f1" stroke-width="1.5"/><path d="M0 4 L10 1 L10 7 Z" fill="#f1f1f1"/></svg>
      <span>www.tavmontgroup.example/blue-forge</span>
      <svg width="48" height="8" viewBox="0 0 48 8"><line x1="0" y1="4" x2="42" y2="4" stroke="#f1f1f1" stroke-width="1.5"/><path d="M48 4 L38 1 L38 7 Z" fill="#f1f1f1"/></svg>
    </div>
  </section>

  <section class="card card-back">
    <div class="accent-dot"></div>
    <h1 class="holder-name">DANIEL HARLOW</h1>
    <p class="holder-title">Managing Director</p>
    <div class="back-mark">BLUE<br>FORGE</div>
    <ul class="contact-list">
      <li><svg viewBox="0 0 16 16"><path d="M2 5 Q8 1 14 5 L12 7 L10 5 H6 L4 7 Z M3 8 H13 L14 14 H2 Z"/></svg>555-010-2468</li>
      <li><svg viewBox="0 0 16 16"><path d="M1 3 H15 V13 H1 Z M2 4 L8 9 L14 4 V5 L8 10 L2 5 Z" fill-rule="evenodd"/></svg>info@tavmontgroup.example</li>
      <li><svg viewBox="0 0 16 16"><circle cx="8" cy="8" r="6.5" fill="none" stroke="#a01c21" stroke-width="1.3"/><ellipse cx="8" cy="8" rx="2.8" ry="6.5" fill="none" stroke="#a01c21" stroke-width="1.2"/><line x1="1.5" y1="8" x2="14.5" y2="8" stroke="#a01c21" stroke-width="1.2"/></svg>www.tavmontgroup.example/blue-forge</li>
    </ul>
    <p class="parent-company">A TAVMONT<br>COMPANY</p>
  </section>
</body>
</html>
```